RKD Cattleworks needs Buisness Card design using new logo

We need a business card design that ties our website and our new logo together. www.rkdcattleworks-example.com The logo will be added to our website at a later date and replace the existing rkd cattleworks that is on the webpage. We are looking for a simple & professional design.

Target Market(s)

Cattle Producers, Ranchers

Industry/Entity Type

Agriculture

Contact Information for Business Card

Side one:
logo
www.rkdcattleworks-example.com

Side two:
RKD Cattleworks
Dennis & Marla Kovacs
Hartney, MB Canada
(555) 316-2984/(555) 472-9051
kovacs47@ploverline-example.net

Font styles to use
Serif
Sans Serif
Script

Requirements
Must have
• We would like to tie our new logo in with our website on the business card.

```html
<!DOCTYPE html>
<html lang="en">
<head>
<meta charset="utf-8">
<title>RKD Cattleworks – Business Card</title>
<link href="https://fonts.googleapis.com/css2?family=Lato:wght@300;400;700&display=swap" rel="stylesheet">
<style>
  :root {
    --stage: #2a2a2a;
    --card-dark: #3a3a3c;
    --card-light: #f4f4f4;
    --ink: #3b3b3d;
    --ink-soft: #4a4a4c;
    --red: #c8161d;
    --white-soft: #e8e8e8;
    --band-dark: #2f2f31;
  }
  * { box-sizing: border-box; margin: 0; padding: 0; }
  html, body { width: 1200px; height: 873px; overflow: hidden; }
  body {
    background: var(--stage);
    font-family: "Lato", Arial, sans-serif;
    position: relative;
  }
  .card {
    position: absolute;
    width: 540px;
    height: 309px;
    border-radius: 3px;
    box-shadow: 0 14px 30px rgba(0,0,0,.45);
    overflow: hidden;
  }
  .card--back {
    left: 70px; top: 110px;
    background: var(--card-dark);
  }
  .card--front {
    left: 590px; top: 450px;
    background: var(--card-light);
  }
  .brand-name {
    position: absolute;
    left: 0; right: 0;
    text-align: center;
    font-weight: 300;
    letter-spacing: 1px;
    white-space: nowrap;
  }
  .card--back .brand-name {
    top: 96px;
    font-size: 50px;
    color: var(--white-soft);
  }
  .card--back .website {
    position: absolute;
    left: 0; right: 0; top: 236px;
    text-align: center;
    font-weight: 700;
    font-size: 19px;
    letter-spacing: 3px;
    color: var(--red);
    white-space: nowrap;
  }
  .card--front .brand-name {
    top: 56px;
    font-size: 42px;
    color: var(--ink);
  }
  .holder {
    position: absolute;
    right: 28px; top: 140px;
    text-align: right;
    white-space: nowrap;
  }
  .holder__name {
    font-weight: 700;
    font-size: 17px;
    color: var(--red);
  }
  .holder__place {
    font-size: 12.5px;
    color: var(--ink);
    margin-top: 3px;
  }
  .contact {
    position: absolute;
    left: 30px; top: 178px;
    list-style: none;
  }
  .contact li {
    display: flex;
    align-items: center;
    gap: 12px;
    font-weight: 700;
    font-size: 14.5px;
    color: var(--ink-soft);
    height: 26px;
    white-space: nowrap;
  }
  .contact svg { width: 15px; height: 15px; fill: var(--red); flex: none; }
  .footer-bands {
    position: absolute;
    left: 0; bottom: 0;
    width: 540px; height: 60px;
  }
</style>
</head>
<body>

  <section class="card card--back" aria-label="Business card, logo side">
    <div class="brand-name">RKD Cattleworks</div>
    <div class="website">www.rkdcattleworks-example.com</div>
  </section>

  <section class="card card--front" aria-label="Business card, contact side">
    <div class="brand-name">RKD Cattleworks</div>

    <div class="holder">
      <div class="holder__name">Dennis &amp; Marla Kovacs</div>
      <div class="holder__place">Hartney, MB Canada</div>
    </div>

    <ul class="contact">
      <li>
        <svg viewBox="0 0 16 16" aria-hidden="true"><path d="M1 5c0-2 2-3 7-3s7 1 7 3v1h-4V5H5v1H1zM3 7h10l1 7H2zm5 2a2 2 0 1 0 0 4 2 2 0 0 0 0-4z"/></svg>
        (555) 316-2984
      </li>
      <li>
        <svg viewBox="0 0 16 16" aria-hidden="true"><path d="M4 1h8v14H4zM5.5 2.5v9h5v-9zM7 12.5h2v1H7z" fill-rule="evenodd"/></svg>
        (555) 472-9051
      </li>
      <li>
        <svg viewBox="0 0 16 16" aria-hidden="true"><path d="M1 3h14v10H1zM2 4l6 5 6-5z" fill-rule="evenodd"/></svg>
        kovacs47@ploverline-example.net
      </li>
    </ul>

    <svg class="footer-bands" viewBox="0 0 540 60" aria-hidden="true">
      <rect x="0" y="42" width="540" height="18" fill="var(--band-dark)"/>
      <path d="M330 60 C340 28 350 22 380 22 L540 4 L540 60 Z" fill="var(--red)"/>
      <path d="M340 60 C348 34 356 30 382 30 L540 14" fill="none" stroke="var(--card-light)" stroke-width="3"/>
    </svg>
  </section>

</body>
</html>
```